Photographic Tutorial website

We are looking for a fresh design for a photographic tutorial / workshop website. The website will have the included functions:

* Home (needs to have a login section)
* About Us
* Info about each course / workshop.
* Subscribe to courses and pay online.
* Members Area
* Photo gallery
* Contact us

The website will be implemented with our own made cms. We do not need it to be coded. We have a team ready to do this for us. We only need the PSD layout.

We have attached a mockup design that the client and I have come up with and we need the design to be taken to the next level.

Client also likes:
http://www.vellowindstudio.example/

Photographic Interests

Online

Requirements
Must have
• Must Stand out i.e black backgrounds
Should not have
• Alter the logo in anyway.

```html
<!DOCTYPE html>
<html lang="en">
<head>
<meta charset="utf-8">
<title>Lens Mate Studio – Photographic Tuition</title>
<link rel="stylesheet" href="https://fonts.googleapis.com/css2?family=Bree+Serif&family=Open+Sans:wght@400;600;700&family=Oswald:wght@400;500;600&display=swap">
<style>
:root{
  --bg:#131313;
  --bg-2:#1b1b1b;
  --panel:#262626;
  --text:#d8d8d8;
  --muted:#8c8c8c;
  --white:#ffffff;
  --orange:#f39a1e;
  --gold:#a8772f;
  --magenta:#b0479c;
  --green:#3a8d1f;
  --rust:#c2421d;
  --yellow:#d9c33a;
  --red:#d94a3a;
  --lime:#7cbf3a;
  --cyan:#3ab8d9;
  --purple:#b04a9a;
  --blue:#2f6fc4;
}
*{margin:0;padding:0;box-sizing:border-box}
html,body{width:1200px;height:2509px;overflow:hidden}
body{position:relative;background:linear-gradient(90deg,#101010,#1a1a1a 30%,#141414 60%,#1b1b1b 85%,#111);color:var(--text);font-family:"Open Sans",Arial,sans-serif;font-size:11px}
.abs{position:absolute}

/* header */
.login{left:980px;top:0;width:74px;height:25px;background:var(--blue);color:#fff;font:600 12px "Open Sans",sans-serif;display:flex;align-items:center;justify-content:center;gap:5px;border-radius:0 0 4px 4px}
.brand{left:145px;top:22px;display:flex;align-items:center;gap:12px}
.brand-dot{width:52px;height:52px;border-radius:50%;background:#c9302c}
.brand-name{font:36px "Bree Serif",serif;color:#fff;line-height:1}
.brand-tag{left:210px;top:64px;font:13px "Open Sans",sans-serif;letter-spacing:4px;color:#e0e0e0;text-transform:uppercase}
.phone{left:830px;top:38px;display:flex;align-items:center;gap:14px}
.phone-text{font:500 28px "Oswald",sans-serif;color:var(--orange)}

.nav{left:145px;top:92px;width:908px;height:38px;background:linear-gradient(#f4f4f4,#c9c9c9);border-radius:5px;display:flex;align-items:center;padding-left:10px}
.nav a{font:600 13px "Open Sans",sans-serif;color:#333;text-decoration:none;padding:0 11px;border-right:1px solid #aaa;line-height:18px}
.nav a:last-child{border:0}
.nav a.active{color:#d9302c}

/* slider */
.slider{left:145px;top:147px;width:908px;height:378px;border-radius:12px;background:linear-gradient(#e8e8e8,#bcbcbc);padding:10px}
.slide{width:100%;height:100%;border-radius:8px;background:linear-gradient(180deg,#3b5d86 0%,#2a3e5e 40%,#4a3b2c 70%,#1a1714 100%);position:relative;overflow:hidden}
.caption{position:absolute;left:0;right:0;bottom:0;height:60px;background:rgba(0,0,0,.55);color:#f0e6c8;font:italic 17px "Bree Serif",serif;padding:18px 28px}
.arrow{width:46px;height:46px;border-radius:50%;background:radial-gradient(#eee,#aaa);border:3px solid #333;top:298px;display:flex;align-items:center;justify-content:center}

/* feature thumbs */
.feature{width:168px;top:556px;text-align:center}
.feature .pic{width:168px;height:130px;border:3px solid;border-radius:4px}
.feature h3{font:600 13px "Oswald",sans-serif;text-transform:uppercase;margin-top:14px;line-height:16px}
.feature p{font-size:10.5px;line-height:14px;color:var(--muted);margin-top:6px;padding:0 6px}

/* section heading */
.section-bar{left:145px;width:667px;height:30px;display:flex;align-items:center;justify-content:space-between;padding:0 14px;color:#fff}
.section-bar h2{font:500 15px "Oswald",sans-serif;text-transform:uppercase;letter-spacing:.5px}
.section-bar span{font:600 11px "Open Sans",sans-serif}

/* post */
.post{left:147px;width:665px;height:200px;border-bottom:1px dotted #444}
.date{width:46px;height:46px;color:#fff;font:700 10px "Open Sans",sans-serif;text-align:center;padding-top:6px;line-height:15px}
.post h3{position:absolute;left:60px;top:10px;font:19px "Bree Serif",serif;color:#fff}
.post .pic{position:absolute;left:0;top:58px;width:107px;height:107px;border:4px solid #3a3a3a}
.post p{position:absolute;left:126px;top:64px;width:535px;font-size:11px;line-height:19px;color:var(--muted)}
.meta{position:absolute;left:126px;top:146px;display:flex;gap:30px;font:italic 10px "Open Sans",sans-serif;color:var(--muted)}
.meta span{display:flex;align-items:center;gap:6px}
.pic-tiger{background:linear-gradient(135deg,#c9822d,#7a4a1c 55%,#3d4b2a)}
.pic-valley{background:linear-gradient(160deg,#8ab0cf,#5d8c3f 45%,#3e5f2b)}

/* sidebar */
.moon{left:850px;top:835px;width:204px;height:84px;background:linear-gradient(#2c63c9,#0f2f7a);border:2px solid #9ab;display:flex;align-items:flex-end;padding:10px;font:17px "Bree Serif",serif;color:#fff}
.twilight{left:850px;top:946px;width:204px;text-align:center;font:700 12px "Open Sans",sans-serif;color:#eee;line-height:17px}
.calendar{left:850px;top:996px;width:204px;background:#2b2b2b;border:1px solid #444}
.cal-head{height:22px;background:#1d1d1d;display:flex;justify-content:space-between;align-items:center;padding:0 10px;color:#fff;font-size:11px}
.cal-grid{display:grid;grid-template-columns:repeat(7,1fr);gap:1px;padding:3px}
.cal-grid b{font:600 8px "Open Sans",sans-serif;color:#bbb;text-align:center;padding:3px 0}
.cal-grid i{font:600 12px "Open Sans",sans-serif;font-style:normal;color:#fff;text-align:center;height:27px;line-height:27px;background:#333}
.cal-grid i.off{color:#777}
.cal-grid i.today{background:#b0151a}
.side-bar{left:850px;width:204px;height:30px;color:#fff;font:600 13px "Open Sans",sans-serif;padding:6px 10px}
.check{left:858px;display:flex;align-items:center;gap:12px;font:700 11px "Bree Serif",serif;color:#eee}
.gallery{left:854px;top:1460px;display:grid;grid-template-columns:repeat(3,59px);gap:11px 11px}
.gallery div{width:59px;height:59px;border:2px solid #555}
.testi-title{left:850px;top:1830px;font:700 12px "Open Sans",sans-serif;color:#eee}
.testi{left:850px;top:1852px;width:204px;height:246px;background:#262626;padding:14px;font:italic 10.5px "Open Sans",sans-serif;line-height:16px;color:var(--muted)}
.testi cite{display:block;text-align:right;color:var(--cyan);margin-top:12px}

/* footer */
.rainbow{left:0;top:2184px;width:1200px;height:4px;background:linear-gradient(90deg,#d9302c,#f39a1e,#d9c33a,#7cbf3a,#3ab8d9,#2f6fc4,#b04a9a)}
.footer{left:0;top:2188px;width:1200px;height:321px;background:#1c1c1c}
.f-contact{left:147px;top:2222px;font:700 11px "Open Sans",sans-serif;color:#fff;line-height:17px}
.f-contact .f-phone{font:500 25px "Oswald",sans-serif;color:var(--orange);margin:4px 0 18px;line-height:30px}
.f-contact .addr{font-weight:400;color:#bbb;line-height:17px}
.f-contact a{color:var(--orange);text-decoration:none;font-weight:400}
.f-courses{left:524px;top:2222px}
.f-courses h4{font:15px "Bree Serif",serif;color:#fff;margin-bottom:14px}
.f-courses li{list-style:none;color:#bbb;font-size:11px;line-height:14px;margin-bottom:13px}
.f-courses li::before{content:"› ";color:#777}
.partner{left:906px;width:140px;height:34px;background:#2c2c2c;border-radius:4px}
.social{top:2457px;width:24px;height:24px;background:#3a3a3a;border-radius:3px}
.copy{left:147px;top:2474px;font:italic 10px "Open Sans",sans-serif;color:#777}
.copy a{color:var(--orange);text-decoration:none}
</style>
</head>
<body>

<div class="abs login">LOGIN <svg width="11" height="11" viewBox="0 0 11 11"><circle cx="5.5" cy="5.5" r="5" fill="none" stroke="#fff"/><path d="M4 3l3 2.5L4 8" stroke="#fff" fill="none"/></svg></div>

<header>
  <div class="abs brand"><span class="brand-dot"></span><span class="brand-name">Lens Mate Studio</span></div>
  <div class="abs brand-tag">Photographic Tuition</div>
  <div class="abs phone">
    <svg width="46" height="40" viewBox="0 0 46 40" aria-hidden="true"><rect x="2" y="6" width="36" height="28" rx="3" fill="#e8e8e8" stroke="#999"/><rect x="6" y="10" width="28" height="20" fill="#5b8fc6"/><path d="M6 30l9-10 7 7 5-5 7 8z" fill="#4a8a2a"/></svg>
    <span class="phone-text">0400 555 018</span>
  </div>
  <nav class="abs nav">
    <a class="active">HOME</a><a>ABOUT US</a><a>COURSE / WORKSHOP</a><a>SUBSCRIBE &amp; PAY ONLINE</a><a>MEMBERS AREA</a><a>PHOTO GALLERY</a><a>CONTACT US</a>
  </nav>
</header>

<section class="abs slider">
  <div class="slide" role="img" aria-label="City skyline of high-rise towers at night">
    <div class="caption">"Neque porro quisquam est qui dolorem ipsum quia dolor tetur, adipisci velit..."</div>
  </div>
</section>
<div class="abs arrow" style="left:121px"><svg width="14" height="14" viewBox="0 0 14 14"><path d="M9 2L4 7l5 5" stroke="#333" stroke-width="2.5" fill="none"/></svg></div>
<div class="abs arrow" style="left:1030px"><svg width="14" height="14" viewBox="0 0 14 14"><path d="M5 2l5 5-5 5" stroke="#333" stroke-width="2.5" fill="none"/></svg></div>

<section>
  <div class="abs feature" style="left:145px"><div class="pic" style="border-color:var(--yellow);background:linear-gradient(#8fb8d8,#7a5a3a 55%,#5a4030)" role="img" aria-label="Wooden pier at the waterfront"></div><h3 style="color:var(--yellow)">Urdan Excursion</h3><p>Lorem Ipsum is simply dummy text of the printing &amp; typesetting industry. Lorem Ipsum has been the industry's standard dummy text ever since the 1500...</p></div>
  <div class="abs feature" style="left:330px"><div class="pic" style="border-color:var(--red);background:linear-gradient(#3e6b4a,#8a4a3a 55%,#2f5a6a)" role="img" aria-label="Row of huts over a lake"></div><h3 style="color:var(--red)">Panorama</h3><p>Lorem Ipsum is simply dummy text of the printing &amp; typesetting industry. Lorem Ipsum has been the industry's standard dummy text ever since the 1500...</p></div>
  <div class="abs feature" style="left:516px"><div class="pic" style="border-color:var(--lime);background:linear-gradient(#1a2a4a,#3a4a7a 50%,#d96a2a)" role="img" aria-label="City street with light trails at night"></div><h3 style="color:var(--lime)">Night Photography<br>&amp; City Lights</h3><p>Lorem Ipsum is simply dummy text of the printing &amp; typesetting industry. Lorem Ipsum has been the industry's standard...</p></div>
  <div class="abs feature" style="left:700px"><div class="pic" style="border-color:var(--cyan);background:linear-gradient(135deg,#9ac8e8,#3a6a9a 60%,#1a3a5a)" role="img" aria-label="Glass office towers seen from below"></div><h3 style="color:var(--cyan)">City Walks</h3><p>Lorem Ipsum is simply dummy text of the printing &amp; typesetting industry. Lorem Ipsum has been the industry's standard dummy text ever since the 1500...</p></div>
  <div class="abs feature" style="left:885px"><div class="pic" style="border-color:var(--purple);background:linear-gradient(#5a7ab8,#c8a8b8 55%,#8a3a3a)" role="img" aria-label="Domed government building under a dramatic sky"></div><h3 style="color:var(--purple)">HDR</h3><p>Lorem Ipsum is simply dummy text of the printing &amp; typesetting industry. Lorem Ipsum has been the industry's standard dummy text ever since the 1500...</p></div>
</section>

<main>
  <div class="abs section-bar" style="top:835px;background:var(--gold)"><h2>General Information &amp; LMS's 2012</h2><span>Read All »</span></div>

  <article class="abs post" style="top:882px"><div class="date" style="background:var(--gold)">JUN 10<br>2011</div><h3>Donec vulputate nulla in nibh pellentesque consequat.</h3><div class="pic pic-tiger" role="img" aria-label="Close-up of a tiger"></div><p>Lorem ipsum dolor sit amet, consectetuer adipiscing elit. Donec semper risus id neque vulp elementum. Ut diam neque, vestibulum non, sagittis quis, commodo id, purus. Vivamus sagittis, odio non rhoncus adipiscing, elit ipsum pulvinar est, vitae malesuada velit orci sed arcu.</p><div class="meta"><span>◷ June 10, 2011</span><span>▭ No Comments</span></div></article>
  <article class="abs post" style="top:1084px"><div class="date" style="background:var(--gold)">JUN 10<br>2011</div><h3>Donec vulputate nulla in nibh pellentesque consequat.</h3><div class="pic pic-tiger" role="img" aria-label="Close-up of a tiger"></div><p>Lorem ipsum dolor sit amet, consectetuer adipiscing elit. Donec semper risus id neque vulp elementum. Ut diam neque, vestibulum non, sagittis quis, commodo id, purus. Vivamus sagittis, odio non rhoncus adipiscing, elit ipsum pulvinar est, vitae malesuada velit orci sed arcu.</p><div class="meta"><span>◷ June 10, 2011</span><span>▭ No Comments</span></div></article>
  <article class="abs post" style="top:1286px"><div class="date" style="background:var(--gold)">JUN 10<br>2011</div><h3>Donec vulputate nulla in nibh pellentesque consequat.</h3><div class="pic pic-tiger" role="img" aria-label="Close-up of a tiger"></div><p>Lorem ipsum dolor sit amet, consectetuer adipiscing elit. Donec semper risus id neque vulp elementum. Ut diam neque, vestibulum non, sagittis quis, commodo id, purus. Vivamus sagittis, odio non rhoncus adipiscing, elit ipsum pulvinar est, vitae malesuada velit orci sed arcu.</p><div class="meta"><span>◷ June 10, 2011</span><span>▭ No Comments</span></div></article>

  <div class="abs section-bar" style="top:1496px;background:var(--magenta)"><h2>USA Fall Travel Tour</h2><span>Read All »</span></div>

  <article class="abs post" style="top:1545px"><div class="date" style="background:var(--magenta)">JUN 10<br>2011</div><h3>Donec vulputate nulla in nibh pellentesque consequat.</h3><div class="pic pic-valley" role="img" aria-label="Green mountain valley with terraces"></div><p>Lorem ipsum dolor sit amet, consectetuer adipiscing elit. Donec semper risus id neque vulp elementum. Ut diam neque, vestibulum non, sagittis quis, commodo id, purus. Vivamus sagittis, odio non rhoncus adipiscing, elit ipsum pulvinar est, vitae malesuada velit orci sed arcu.</p><div class="meta"><span>◷ June 10, 2011</span><span>▭ No Comments</span></div></article>
  <article class="abs post" style="top:1747px"><div class="date" style="background:var(--magenta)">JUN 10<br>2011</div><h3>Donec vulputate nulla in nibh pellentesque consequat.</h3><div class="pic pic-valley" role="img" aria-label="Green mountain valley with terraces"></div><p>Lorem ipsum dolor sit amet, consectetuer adipiscing elit. Donec semper risus id neque vulp elementum. Ut diam neque, vestibulum non, sagittis quis, commodo id, purus. Vivamus sagittis, odio non rhoncus adipiscing, elit ipsum pulvinar est, vitae malesuada velit orci sed arcu.</p><div class="meta"><span>◷ June 10, 2011</span><span>▭ No Comments</span></div></article>
  <article class="abs post" style="top:1949px;border-bottom:0"><div class="date" style="background:var(--magenta)">JUN 10<br>2011</div><h3>Donec vulputate nulla in nibh pellentesque consequat.</h3><div class="pic pic-valley" role="img" aria-label="Green mountain valley with terraces"></div><p>Lorem ipsum dolor sit amet, consectetuer adipiscing elit. Donec semper risus id neque vulp elementum. Ut diam neque, vestibulum non, sagittis quis, commodo id, purus. Vivamus sagittis, odio non rhoncus adipiscing, elit ipsum pulvinar est, vitae malesuada velit orci sed arcu.</p><div class="meta"><span>◷ June 10, 2011</span><span>▭ No Comments</span></div></article>
</main>

<aside>
  <div class="abs moon" role="img" aria-label="Night sky with crescent moon and clouds">Moon Phase Chart</div>
  <div class="abs twilight">Daily Shooting Times Nautical<br>Twilight Start to End</div>
  <div class="abs calendar">
    <div class="cal-head"><span>◂</span><span>July 2012</span><span>▸</span></div>
    <div class="cal-grid">
      <b>MON</b><b>TUE</b><b>WED</b><b>THU</b><b>FRI</b><b>SAT</b><b>SUN</b>
      <i class="off">26</i><i class="off">27</i><i class="off">28</i><i class="off">29</i><i class="off">30</i><i class="off">1</i><i>2</i>
      <i>3</i><i>4</i><i>5</i><i>6</i><i>7</i><i>8</i><i>9</i>
      <i>10</i><i>11</i><i>12</i><i>13</i><i>14</i><i>15</i><i>16</i>
      <i>17</i><i>18</i><i>19</i><i>20</i><i>21</i><i class="today">22</i><i>23</i>
      <i>24</i><i>25</i><i>26</i><i>27</i><i>28</i><i>29</i><i>30</i>
      <i>31</i>
    </div>
  </div>

  <div class="abs side-bar" style="top:1250px;background:var(--green)">Photograpers Check Lists</div>
  <div class="abs check" style="top:1295px"><svg width="20" height="18" viewBox="0 0 20 18"><rect x="1" y="1" width="18" height="13" rx="3" fill="none" stroke="#aaa" stroke-width="2"/><path d="M5 14l-2 4 6-4" fill="#aaa"/></svg>Wedding Shoot Check list</div>
  <div class="abs check" style="top:1327px"><svg width="20" height="18" viewBox="0 0 20 18"><rect x="1" y="1" width="18" height="13" rx="3" fill="none" stroke="#aaa" stroke-width="2"/><path d="M5 14l-2 4 6-4" fill="#aaa"/></svg>Pre Shoot Check list</div>
  <div class="abs check" style="top:1359px"><svg width="20" height="18" viewBox="0 0 20 18"><rect x="1" y="1" width="18" height="13" rx="3" fill="none" stroke="#aaa" stroke-width="2"/><path d="M5 14l-2 4 6-4" fill="#aaa"/></svg>Standard Check list</div>

  <div class="abs side-bar" style="top:1410px;background:var(--rust)">Members Gallery</div>
  <div class="abs gallery" role="img" aria-label="Grid of member photographs: flowers, canyons, wildlife and landscapes">
    <div style="background:linear-gradient(#d8d890,#6a8a3a)"></div><div style="background:linear-gradient(#c86a2a,#6a2a1a)"></div><div style="background:linear-gradient(#c8c8c8,#6a6a5a)"></div>
    <div style="background:linear-gradient(#f0c020,#b06a10)"></div><div style="background:linear-gradient(#3a5ac8,#d8a040)"></div><div style="background:linear-gradient(#7a9ab8,#3a4a5a)"></div>
    <div style="background:linear-gradient(#c86a2a,#3a2a1a)"></div><div style="background:linear-gradient(#e8f0f8,#2a4a7a)"></div><div style="background:linear-gradient(#d81a1a,#6a0a0a)"></div>
    <div style="background:linear-gradient(#d8d890,#6a8a3a)"></div><div style="background:linear-gradient(#c86a2a,#6a2a1a)"></div><div style="background:linear-gradient(#c8c8c8,#6a6a5a)"></div>
    <div style="background:linear-gradient(#f0c020,#b06a10)"></div><div style="background:linear-gradient(#3a5ac8,#d8a040)"></div><div style="background:linear-gradient(#7a9ab8,#3a4a5a)"></div>
  </div>

  <div class="abs testi-title">Testimonials</div>
  <div class="abs testi">Lorem ipsum dolor sit consectetuer adipiscing elit. Donec semper risus id neque vulp elementum. Ut diam neque, ollum non, sagittis quis, comhivamus adiping, elit ipsum pulvinar est, vitae malesuada velit orci sed arcu. Lorem ipsum dolor sit consec-tetuer adipiscing elit. Donec semper risus id neque sudet elementum.<cite>- Dana Whitfield</cite></div>
</aside>

<footer>
  <div class="abs footer"></div>
  <div class="abs rainbow"></div>
  <div class="abs f-contact">For more info about our courses,<br>please contact
    <div class="f-phone">0400 555 018</div>
    <div class="addr">246 Lorem Lipsum 112 st,<br>MA 01234, Australia,<br>FAX: 0123 456 7890<br>Email: <a>info@lensmatestudio.example</a></div>
  </div>
  <div class="abs f-courses">
    <h4>OUR COURSES</h4>
    <ul>
      <li>Night Photography</li>
      <li>Leagrning the basics of Exposure,<br>Aventure, ISO &amp; compresition</li>
      <li>Learning your camera funcations</li>
      <li>How to pick that good spot</li>
      <li>What equipment do I need</li>
    </ul>
  </div>
  <div class="abs partner" style="top:2222px"></div>
  <div class="abs partner" style="top:2270px"></div>
  <div class="abs partner" style="top:2318px"></div>
  <div class="abs partner" style="top:2366px"></div>
  <div class="abs social" style="left:962px"></div>
  <div class="abs social" style="left:992px"></div>
  <div class="abs social" style="left:1022px"></div>
  <div class="abs copy">Copyright © 2012 Lens Mate Studio, All Rights Reserved. <a>Links &amp; Reviews</a></div>
</footer>

</body>
</html>
```